Website design needed for gift based dropship website

I am building a dropshipping website that will create gift based merchandise and send it out to our clients customers for them. Our clients will sell products and when a customer buys from them, we create the item and send it out to the customer.

I am looking for a very similar website to quillmarten.com - that website is doing a very similar thing to what i am doing but where the quillmarten website is based around clothing, my website will be based around gifts. Another website that i like that is doing a similar thing to what i will do is dravo.com

I require 2 pages to be made:
1) The home page
2) A landing page for a free product giveaway offer

1) THE HOME PAGE
The home page should be a merger of the two previously stated websites (www.dravo.com and www.quillmarten.com). The style fo the homepage should be based on the logo that is attached and the colour scheme should be similar but basic.

2) THE LANDING PAGE
The landing page will be giving away a free mobile phone cover. The page needs to have some mobile phone covers for different phones all with random designs on. The page should state that they can have any design that they want and they do not pay for the phone (they only pay for shipping).

Menu pages and text should be taken from the quillmarten.com website.

Target Market(s)

18 - 40 year old males. People who like the idea of earning extra money in their spare time but aren't too sure how to do it. Semi-professional jobs.

Number of Pages Required

2 page

Font styles to use
Serif
Sans Serif
Decorative
Script

Colors

Designer to choose colors to be used in the design.

Requirements
Must have
• A "how it works" image where the dropshipping process is explained to a visitor to the website (similar to the one on the quillmarten "how it works page")
Nice to have
• Testimonial area on homepage
Should not have
• Homepage should not have:
• - "latest orders from" area
• - Video
• - Warehousing/fulfilment area
• - Integration area
• -

```html
<!DOCTYPE html>
<html lang="en">
<head>
<meta charset="utf-8">
<title>Giftloom – On-demand gift printing</title>
<link href="https://fonts.googleapis.com/css2?family=Oswald:wght@400;500;600&family=Open+Sans:wght@400;600;700&display=swap" rel="stylesheet">
<style>
:root{
  --red:#e8402d;
  --red-dark:#8e2a2e;
  --red-mid:#c8353a;
  --ink:#2b2b2b;
  --text:#555;
  --muted:#8a8a8a;
  --line:#e3e3e3;
  --soft:#f4f4f4;
  --card:#f7f7f7;
  --white:#fff;
}
*{box-sizing:border-box;margin:0;padding:0}
html,body{width:1200px;height:3651px;overflow:hidden}
body{font-family:"Open Sans",Arial,sans-serif;color:var(--text);background:var(--white);font-size:13px;line-height:1.6}
.wrap{width:732px;margin:0 auto;position:relative}
h1,h2,h3,h4,.brand,.btn,.nav a{font-family:"Oswald","Arial Narrow",sans-serif}
.section-title{font-size:21px;font-weight:500;color:var(--ink);text-align:center;letter-spacing:.3px;text-transform:uppercase}
.section-sub{text-align:center;font-size:13px;color:var(--text);margin-top:2px}
.btn{display:inline-block;font-size:13px;text-transform:uppercase;letter-spacing:.4px;padding:8px 20px;border-radius:2px;text-decoration:none}
.btn-red{background:var(--red);color:var(--white)}
.btn-ghost{border:1px solid #bbb;color:#777;background:var(--white)}
.btn-outline-white{border:1px solid var(--white);color:var(--white)}
.brand{display:flex;align-items:center;gap:8px;color:var(--red-dark);font-weight:600;font-size:22px;text-transform:uppercase;letter-spacing:.5px;text-decoration:none}
.brand-dot{width:26px;height:26px;border-radius:50%;background:var(--red)}

/* header */
.site-header{height:68px;border-bottom:1px solid var(--line)}
.site-header .wrap{height:68px;display:flex;justify-content:space-between;align-items:center}
.header-right{display:flex;flex-direction:column;align-items:flex-end;gap:6px}
.topbar{font-size:10px;color:var(--muted);display:flex;gap:14px}
.topbar b{color:var(--red)}
.nav{display:flex;gap:18px}
.nav a{font-size:14px;color:var(--ink);text-decoration:none;text-transform:uppercase;padding-bottom:4px}
.nav a.active{color:var(--red);border-bottom:2px solid var(--red)}

/* hero */
.hero{height:317px;background:repeating-linear-gradient(90deg,rgba(255,255,255,.03) 0 3px,transparent 3px 7px),linear-gradient(90deg,var(--red-dark),var(--red-mid) 50%,var(--red));position:relative;text-align:center;color:var(--white);padding-top:32px}
.badge{display:inline-block;background:var(--red);font-family:"Oswald",sans-serif;font-size:15px;padding:2px 12px;text-transform:uppercase}
.hero h1{font-size:32px;font-weight:500;letter-spacing:1px;text-transform:uppercase;margin-top:6px;line-height:1.2}
.hero p{font-size:14px;margin:2px 0 14px}
.hero-gifts{position:absolute;left:414px;bottom:0;width:377px;height:93px;background:linear-gradient(180deg,#e8e8e8,#cfcfcf);border-radius:4px 4px 0 0}

/* split */
.split{height:192px;display:flex;position:relative}
.split-col{flex:1;text-align:center;padding-top:40px}
.split-col.alt{background:var(--soft)}
.split-col h3{font-size:16px;font-weight:500;color:var(--ink);text-transform:uppercase}
.split-col p{font-size:12px;width:230px;margin:8px auto 14px;line-height:1.55}
.or{position:absolute;left:585px;top:82px;width:30px;height:30px;border-radius:50%;background:var(--white);font-family:"Oswald",sans-serif;font-size:11px;color:var(--ink);line-height:30px;text-align:center}

/* products */
.products{height:725px;padding-top:42px;text-align:center}
.grid{display:grid;grid-template-columns:repeat(4,175px);gap:15px 10px;margin-top:40px;text-align:center}
.card{border:1px solid var(--line);height:246px;display:flex;flex-direction:column}
.card-media{height:180px;background:var(--white);display:flex;align-items:center;justify-content:center}
.card-media div{width:90px;height:130px;border-radius:6px}
.card-info{flex:1;background:var(--card);padding-top:10px;position:relative}
.card-info h4{font-size:13px;font-weight:500;color:var(--ink);text-transform:uppercase}
.card-info span{font-size:10px;color:var(--muted)}
.card-info span b{color:var(--red);font-weight:400}
.card.featured .card-info{background:var(--red);text-align:left;padding-left:10px}
.card.featured h4,.card.featured span,.card.featured span b{color:var(--white)}
.card-arrow{position:absolute;right:14px;top:18px;width:26px;height:26px;border:1.5px solid var(--white);border-radius:50%}
.products .btn{margin-top:36px}

/* how it works */
.how{height:389px;background:linear-gradient(160deg,#f1f1f1 0 40%,#fafafa 40% 60%,#f1f1f1 60%);padding-top:38px;text-align:center}
.steps{display:flex;justify-content:space-between;margin-top:30px}
.step{width:210px}
.step-icon{width:120px;height:120px;border:2px solid var(--red-dark);border-radius:50%;margin:0 auto;display:flex;align-items:center;justify-content:center;background:var(--white)}
.step h4{font-size:14px;font-weight:400;color:var(--red);text-transform:uppercase;margin:14px 0 6px}
.step p{font-size:11px;line-height:1.6;color:var(--text);text-align:justify;text-align-last:center}
.step-arrow{position:absolute;width:90px;height:2px;background:#bbb}
.step-arrow::after{content:"";position:absolute;right:-2px;top:-4px;border-left:8px solid #bbb;border-top:5px solid transparent;border-bottom:5px solid transparent}

/* testimonials */
.reviews{height:504px;padding-top:38px;text-align:center}
.quote-icon{width:50px;height:50px;margin:18px auto 0;border:2px solid var(--red);border-radius:50%;display:flex;align-items:center;justify-content:center}
.review-row{display:flex;justify-content:space-between;margin-top:28px}
.review{width:230px}
.review-box{height:180px;border:1px solid var(--line);box-shadow:0 2px 6px rgba(0,0,0,.06);padding:18px 16px 0}
.stars{color:var(--red);font-size:13px;letter-spacing:2px}
.review-box p{font-size:11px;line-height:1.65;text-align:justify;text-align-last:center;margin-top:8px}
.review-name{font-size:10px;color:var(--red);text-transform:uppercase;margin-top:12px}
.reviews .btn{margin-top:30px}

/* difference */
.diff{height:392px;background:repeating-linear-gradient(90deg,rgba(255,255,255,.035) 0 3px,transparent 3px 7px),linear-gradient(90deg,var(--red-dark),var(--red-mid) 45%,var(--red));color:var(--white);position:relative;padding-top:44px;text-align:center}
.diff .section-title{color:var(--white)}
.diff .section-sub{color:var(--white)}
.diff-photo{position:absolute;left:183px;bottom:0;width:279px;height:372px;background:linear-gradient(180deg,#c9a78a,#8b6a4c 55%,#5a3c45);border-radius:4px 4px 0 0}
.features{position:absolute;left:487px;top:141px;width:486px;display:grid;grid-template-columns:1fr 1fr;gap:26px 22px;text-align:left}
.feature{display:flex;gap:8px}
.feature .num{font-family:"Oswald",sans-serif;font-size:26px;line-height:1}
.feature h4{font-size:13px;font-weight:500;text-transform:uppercase}
.feature p{font-size:10.5px;line-height:1.65;margin-top:4px}

/* signup */
.signup{height:460px;padding-top:40px}
.signup-body{display:flex;justify-content:space-between;margin-top:38px}
.perks{width:360px;list-style:none}
.perks li{margin-bottom:28px}
.perks h4{font-size:13px;font-weight:500;color:var(--ink);text-transform:uppercase;display:flex;align-items:center;gap:8px}
.perks h4::before{content:"";width:10px;height:10px;border:2px solid var(--red);border-radius:50%}
.perks p{font-size:11px;line-height:1.6;margin-left:18px}
.signup-form{width:260px;height:268px;border:1px solid var(--line);text-align:center}
.signup-form h3{background:var(--soft);font-size:17px;font-weight:400;color:var(--ink);text-transform:uppercase;padding:10px 0}
.field{display:block;width:216px;height:30px;margin:10px auto 0;border:1px solid var(--line);font-size:11px;color:var(--muted);text-align:left;padding:6px 10px;background:var(--white)}
.field.shaded{background:#f9f9f9;border-color:#f9f9f9}
.signup-form .btn{margin-top:14px}
.terms{font-size:8.5px;color:var(--ink);margin-top:16px}

/* newsletter */
.newsletter{height:148px;background:var(--soft)}
.newsletter .wrap{display:flex;justify-content:space-between;padding-top:40px}
.newsletter h3{font-size:22px;font-weight:500;color:var(--ink);text-transform:uppercase}
.newsletter p{font-size:11px;line-height:1.6;width:420px}
.news-form{display:flex;margin-top:10px;height:42px}
.news-input{width:260px;border:1px solid var(--line);background:var(--white);font-size:11px;color:var(--muted);padding:12px}
.news-send{width:44px;background:var(--red);display:flex;align-items:center;justify-content:center}

/* footer */
.site-footer{height:431px;padding-top:34px}
.site-footer .brand{justify-content:center}
.footer-cols{display:flex;border-top:1px solid var(--line);margin-top:28px;padding-top:24px;font-size:10.5px;line-height:19px}
.footer-cols ul{list-style:none}
.footer-cols li{white-space:nowrap}
.col-contact{width:214px}
.col-contact li{display:flex;gap:8px;margin-bottom:6px}
.col-contact svg{flex:none;margin-top:3px}
.col-a{width:234px}.col-b{width:163px}
.social{display:flex;justify-content:center;gap:6px;margin-top:34px}
.social span{width:24px;height:24px;border-radius:50%;background:var(--red)}
.copy{text-align:center;font-size:10px;margin-top:6px;color:var(--text)}
</style>
</head>
<body>

<header class="site-header">
  <div class="wrap">
    <a class="brand" href="#"><span class="brand-dot"></span>Giftloom</a>
    <div class="header-right">
      <div class="topbar"><span>CALL FOR ENQUIRY: <b>0123 555 0199</b></span><span>SIGN IN</span><span>SIGN UP</span></div>
      <nav class="nav">
        <a class="active" href="#">Products &amp; Pricing</a><a href="#">How it works</a><a href="#">Shipping</a><a href="#">Resources</a><a href="#">FAQ</a><a href="#">Blog</a>
      </nav>
    </div>
  </div>
</header>

<section class="hero">
  <span class="badge">Hurry up! 10% off</span>
  <h1>We print all kind of gifts</h1>
  <p>Easy, on-demand, online printing, fulfillment and shipping.</p>
  <a class="btn btn-outline-white" href="#">Get started</a>
  <div class="hero-gifts" role="img" aria-label="Illustration of wrapped gift boxes with red ribbons"></div>
</section>

<section class="split">
  <div class="split-col">
    <h3>Print designs for yourself</h3>
    <p>One-off designs that you want to have printed for your own use</p>
    <a class="btn btn-ghost" href="#">Get started</a>
  </div>
  <div class="split-col alt">
    <h3>Sell designs online</h3>
    <p>If you want to sell your designs in an online store or marketplace</p>
    <a class="btn btn-red" href="#">Connect your shop</a>
  </div>
  <span class="or">OR</span>
</section>

<section class="products">
  <div class="wrap">
    <h2 class="section-title">Our custom printed products</h2>
    <p class="section-sub">Lorem ipsum dolor sit amet, consectetur adipiscing elit</p>
    <div class="grid">
      <article class="card featured">
        <div class="card-media"><div role="img" aria-label="Backpack with geometric print" style="background:linear-gradient(135deg,#3aa7a5,#e8574a 55%,#f0c9b0)"></div></div>
        <div class="card-info"><h4>Backpacks</h4><span>Starting from <b>$26.90</b></span><i class="card-arrow"></i></div>
      </article>
      <article class="card">
        <div class="card-media"><div role="img" aria-label="Framed poster with bird print" style="background:#ececec;border:6px solid #222;border-radius:0;width:110px"></div></div>
        <div class="card-info"><h4>Posters &amp; canvas prints</h4><span>Starting from <b>$7</b></span></div>
      </article>
      <article class="card">
        <div class="card-media"><div role="img" aria-label="Coffee mug with geometric print" style="background:linear-gradient(135deg,#4fb3ad,#f08a6b 50%,#f4d0b4);height:70px;width:110px"></div></div>
        <div class="card-info"><h4>Coffee mugs</h4><span>Starting from <b>$8.90</b></span></div>
      </article>
      <article class="card">
        <div class="card-media"><div role="img" aria-label="Phone case with geometric print" style="background:linear-gradient(135deg,#f2c6b2,#e8574a 50%,#3aa7a5);width:60px;border-radius:10px"></div></div>
        <div class="card-info"><h4>Phone case</h4><span>Starting from <b>$15.90</b></span></div>
      </article>
      <article class="card">
        <div class="card-media"><div role="img" aria-label="Throw pillow with small triangle pattern" style="background:#f3f1ee;width:120px;height:110px"></div></div>
        <div class="card-info"><h4>Throw pillows</h4><span>Starting from <b>$12</b></span></div>
      </article>
      <article class="card">
        <div class="card-media"><div role="img" aria-label="Tote bag with dotted print" style="background:#f3f1ee;width:100px;height:110px;border-radius:2px"></div></div>
        <div class="card-info"><h4>Tote bags</h4><span>Starting from <b>$12</b></span></div>
      </article>
      <article class="card">
        <div class="card-media"><div role="img" aria-label="Framed poster with bird print" style="background:#ececec;border:6px solid #222;border-radius:0;width:110px"></div></div>
        <div class="card-info"><h4>Posters &amp; canvas prints</h4><span>Starting from <b>$7</b></span></div>
      </article>
      <article class="card">
        <div class="card-media"><div role="img" aria-label="Backpack with geometric print" style="background:linear-gradient(135deg,#3aa7a5,#e8574a 55%,#f0c9b0)"></div></div>
        <div class="card-info"><h4>Backpacks</h4><span>Starting from <b>$26.90</b></span></div>
      </article>
    </div>
    <a class="btn btn-red" href="#">Load more products</a>
  </div>
</section>

<section class="how">
  <div class="wrap">
    <h2 class="section-title">How it works</h2>
    <p class="section-sub">Lorem ipsum dolor sit amet, consectetur adipiscing elit</p>
    <div class="steps">
      <div class="step">
        <div class="step-icon">
          <svg width="60" height="60" viewBox="0 0 60 60" fill="none" stroke="#8e2a2e" stroke-width="2.5"><path d="M8 22h44l-4-10H12z"/><path d="M8 22c0 4 7 4 7 0 0 4 7 4 7 0 0 4 8 4 8 0 0 4 7 4 7 0 0 4 8 4 8 0 0 4 7 4 7 0"/><rect x="11" y="28" width="38" height="24"/><rect x="17" y="33" width="12" height="10"/><rect x="34" y="33" width="10" height="19"/></svg>
        </div>
        <h4>Your store</h4>
        <p>Lorem ipsum dolor sit amet, consectetur adipiscing elit. Proin cursus eget sapien id eleifend. Morbi gravida malesuada venenatis fusce consectetur pulvinar.</p>
      </div>
      <div class="step">
        <div class="step-icon">
          <svg width="60" height="60" viewBox="0 0 60 60" fill="none" stroke="#8e2a2e" stroke-width="2.5"><rect x="10" y="32" width="40" height="18"/><path d="M6 50h48"/><rect x="22" y="14" width="16" height="14"/><path d="M22 21h16M30 14v-6"/><path d="M16 40h8M36 40h8"/></svg>
        </div>
        <h4>Quillmarten factory</h4>
        <p>Lorem ipsum dolor sit amet, consectetur adipiscing elit. Proin cursus eget sapien id eleifend. Morbi gravida malesuada venenatis fusce consectetur pulvinar.</p>
      </div>
      <div class="step">
        <div class="step-icon">
          <svg width="60" height="60" viewBox="0 0 60 60" fill="none" stroke="#8e2a2e" stroke-width="2.5"><circle cx="30" cy="20" r="10"/><path d="M12 52c0-11 8-18 18-18s18 7 18 18z"/><path d="M18 14h24"/></svg>
        </div>
        <h4>Your client</h4>
        <p>Lorem ipsum dolor sit amet, consectetur adipiscing elit. Proin cursus eget sapien id eleifend. Morbi gravida malesuada venenatis fusce consectetur pulvinar.</p>
      </div>
    </div>
    <span class="step-arrow" style="left:190px;top:200px"></span>
    <span class="step-arrow" style="left:452px;top:200px"></span>
  </div>
</section>

<section class="reviews">
  <div class="wrap">
    <h2 class="section-title">What our customers speak</h2>
    <p class="section-sub">Lorem ipsum dolor sit amet, consectetur adipiscing elit</p>
    <div class="quote-icon"><svg width="24" height="20" viewBox="0 0 24 20" fill="none" stroke="#e8402d" stroke-width="2"><path d="M2 18V10c0-5 3-8 8-8M14 18V10c0-5 3-8 8-8"/><rect x="2" y="10" width="7" height="8"/><rect x="14" y="10" width="7" height="8"/></svg></div>
    <div class="review-row">
      <div class="review"><div class="review-box"><div class="stars">☆☆☆☆☆</div><p>Nunc accumsan leo quam, vel suscipit leo lobortis ut. Suspendisse eget hendrerit quam. Curabitur in odio nec libero ullamcorper iaculis. Praesent ornare augue ut ante congue dapibus. Integer luctus mollis viverra.</p></div><div class="review-name">John Smith</div></div>
      <div class="review"><div class="review-box"><div class="stars">☆☆☆☆☆</div><p>Nunc accumsan leo quam, vel suscipit leo lobortis ut. Suspendisse eget hendrerit quam. Curabitur in odio nec libero ullamcorper iaculis. Praesent ornare augue ut ante congue dapibus. Integer luctus mollis viverra.</p></div><div class="review-name">John Smith</div></div>
      <div class="review"><div class="review-box"><div class="stars">☆☆☆☆☆</div><p>Nunc accumsan leo quam, vel suscipit leo lobortis ut. Suspendisse eget hendrerit quam. Curabitur in odio nec libero ullamcorper iaculis. Praesent ornare augue ut ante congue dapibus. Integer luctus mollis viverra.</p></div><div class="review-name">John Smith</div></div>
    </div>
    <a class="btn btn-red" href="#">Read all testimonials</a>
  </div>
</section>

<section class="diff">
  <h2 class="section-title">What makes us different</h2>
  <p class="section-sub">Lorem ipsum dolor sit amet, consectetur adipiscing elit</p>
  <div class="diff-photo" role="img" aria-label="Photo of a smiling man carrying branded cardboard boxes"></div>
  <div class="features">
    <div class="feature"><span class="num">01.</span><div><h4>Three fulfillment locations</h4><p>Nunc accumsan leo quam, vel suscipit leo lobortis ut. Suspendisse eget hendrerit quam. Curabitur in odio nec libero ullamcorper iaculis.</p></div></div>
    <div class="feature"><span class="num">02.</span><div><h4>Free signup, no monthly fees</h4><p>Nunc accumsan leo quam, vel suscipit leo lobortis ut. Suspendisse eget hendrerit quam. Curabitur in odio nec libero ullamcorper iaculis.</p></div></div>
    <div class="feature"><span class="num">03.</span><div><h4>Automated order import</h4><p>Nunc accumsan leo quam, vel suscipit leo lobortis ut. Suspendisse eget hendrerit quam. Curabitur in odio nec libero ullamcorper iaculis.</p></div></div>
    <div class="feature"><span class="num">04.</span><div><h4>Low shipping rates</h4><p>Nunc accumsan leo quam, vel suscipit leo lobortis ut. Suspendisse eget hendrerit quam. Curabitur in odio nec libero ullamcorper iaculis.</p></div></div>
  </div>
</section>

<section class="signup">
  <div class="wrap">
    <h2 class="section-title">Create your Giftloom account for free</h2>
    <p class="section-sub">Lorem ipsum dolor sit amet, consectetur adipiscing elit</p>
    <div class="signup-body">
      <ul class="perks">
        <li><h4>No sign-up &amp; no monthly fees</h4><p>Nunc accumsan leo quam, vel suscipit leo lobortis ut. Suspendisse eget hendrerit quam. Curabitur in odio nec libero ullamcorper iaculis.</p></li>
        <li><h4>Discounts on sample orders</h4><p>Nunc accumsan leo quam, vel suscipit leo lobortis ut. Suspendisse eget hendrerit quam. Curabitur in odio nec libero ullamcorper iaculis.</p></li>
        <li><h4>More time for yourself</h4><p>Nunc accumsan leo quam, vel suscipit leo lobortis ut. Suspendisse eget hendrerit quam. Curabitur in odio nec libero ullamcorper iaculis.</p></li>
      </ul>
      <div class="signup-form">
        <h3>Free sign up</h3>
        <span class="field">Full Name</span>
        <span class="field shaded">Email</span>
        <span class="field shaded">Password</span>
        <a class="btn btn-red" href="#">Submit</a>
        <p class="terms">By signing up you agree with Terms and Privacy Policy</p>
      </div>
    </div>
  </div>
</section>

<section class="newsletter">
  <div class="wrap">
    <div>
      <h3>Newsletter subscription</h3>
      <p>Nunc accumsan leo quam, vel suscipit leo lobortis ut. Suspendisse eget hendrerit quam. Curabitur in odio nec libero ullamcorper iaculis.</p>
    </div>
    <div class="news-form">
      <span class="news-input">Email Address</span>
      <span class="news-send"><svg width="18" height="18" viewBox="0 0 18 18" fill="#fff"><path d="M1 8l16-7-6 16-2-7z"/></svg></span>
    </div>
  </div>
</section>

<footer class="site-footer">
  <div class="wrap">
    <a class="brand" href="#"><span class="brand-dot"></span>Giftloom</a>
    <div class="footer-cols">
      <ul class="col-contact">
        <li><svg width="10" height="12" viewBox="0 0 10 12" fill="#e8402d"><path d="M5 0a4 4 0 014 4c0 3-4 8-4 8S1 7 1 4a4 4 0 014-4z"/></svg><span>48 Larkfield Row, Ashbury,<br>Vermont 05301</span></li>
        <li><svg width="10" height="12" viewBox="0 0 10 12" fill="none" stroke="#e8402d" stroke-width="1.5"><path d="M2 1h2l1 3-1.5 1a6 6 0 003 3L8 7l2 1v2c-5 1-10-4-8-9z"/></svg><span>0123 555 0199</span></li>
        <li><svg width="10" height="12" viewBox="0 0 10 12" fill="none" stroke="#e8402d" stroke-width="1.3"><rect x="0.5" y="3" width="9" height="6"/><path d="M0.5 3l4.5 3.5L9.5 3"/></svg><span>hello@giftloom-mail.com</span></li>
      </ul>
      <ul class="col-a"><li>Quality</li><li>Products &amp; Pricing</li><li>Volume discounts</li><li>Upcoming products</li><li>Shipping</li><li>Warehousing &amp; Fulfillment New</li><li>API</li><li>Mockup Generator</li><li>Policies</li></ul>
      <ul class="col-b"><li>About us</li><li>Jobs New</li><li>Customers</li><li>Press</li><li>Blog</li><li>Reviews</li><li>Checklist</li><li>Profit Calculator</li><li>Feature Requests</li><li>Sitemap</li></ul>
      <ul><li>FAQ</li><li>Merchandise</li><li>Affiliate</li><li>Quillmarten for production</li><li>Important printing facts</li><li>Fabric printing guide</li><li>Screen printing</li></ul>
    </div>
    <div class="social"><span></span><span></span><span></span></div>
    <p class="copy">2018 © Copyright, Giftloom. All Rights Reserved</p>
  </div>
</footer>

</body>
</html>
```